vale corvan website design

An IT support and IT Security Company - just use dummy text for now for the design. Examples of sites we like the looks and feel of but need it more professional feel are like: www.brontahelpdesk.uk.com , www.quillmoor.co.uk, www.harvestine.com/professional/, www.dulo.com, www.fenwix.com,

Best to message me if you have any questions

Target Market(s)

small to medium UK based companies that require IT support services

Industry/Entity Type

It Company

Contact Information for Business Card

use dummy name, telephone and email for now, will provide details later.

Logo Text

vale corvan (and then below the logo it should say "your IT, networks and security partner")

Coding

Coded - Design and coding required

Number of Pages Required

5+ page

Colors

Designer to choose colors to be used in the design.

Requirements
Must have
• must be professional, yet simple and clear that this is a serious IT support and IT security company.
Nice to have
• 1)The website homepage must have professional quality pictures of IT support or London city skyline or any picture that projects friendly business partners, professionalism and ready to serve.
• 2) Home page needs to include tabs for following pages 'Services' , 'About Us' , 'Contact Us' 'Home'
• 3) Website built customised using wordpress is ideal and easy for us to manage.
• more room for boxed options from homepage (with pic or image in background)
Should not have
• no checkout trolleys or payment options.

```html
<!DOCTYPE html>
<html lang="en">
<head>
<meta charset="utf-8">
<title>Vale Corvan – IT Support &amp; Security</title>
<link href="https://fonts.googleapis.com/css2?family=Lato:wght@300;400;700&display=swap" rel="stylesheet">
<style>
:root{
  --ink:#222;
  --text:#444;
  --muted:#777;
  --light:#f3f3f3;
  --white:#fff;
  --accent-red:#e0313f;
  --yellow:#f5b129;
  --orange:#cc6a35;
  --teal:#3f8a8e;
  --pink:#ee4f6a;
  --green:#2fa58f;
  --blue-line:#4f80c6;
  --divider:#dcdcdc;
}
*{box-sizing:border-box;margin:0;padding:0}
html,body{width:1200px;height:2740px;overflow:hidden}
body{font-family:'Lato',sans-serif;color:var(--text);background:var(--white);position:relative}
a{color:inherit;text-decoration:none}

.topbar{height:47px;background:var(--light);display:flex;align-items:center;padding:0 75px;font-size:12px;font-weight:700;color:#444;letter-spacing:.3px}
.topbar .call{display:flex;align-items:center;gap:10px}
.topbar .social{margin-left:auto;display:flex;gap:14px;margin-right:24px}
.social span{width:14px;height:14px;border-radius:50%;background:#8a8a8a;display:block}
.login{height:47px;background:var(--yellow);color:var(--white);display:flex;align-items:center;gap:8px;padding:0 18px;font-size:11px;margin-right:-2px}

.header{height:110px;display:flex;align-items:center;padding:0 75px}
.brand{font-size:44px;font-weight:400;color:var(--ink);letter-spacing:.3px}
.nav{margin-left:auto;display:flex;gap:30px;font-size:12px;font-weight:700;color:#333}
.nav .active{color:var(--accent-red)}

.hero{position:relative;height:519px;background:linear-gradient(180deg,#55677a 0%,#7d8690 35%,#a08c72 70%,#7a6650 100%);text-align:center;color:var(--white)}
.hero h1{position:absolute;top:182px;left:0;right:0;font-size:64px;font-weight:700}
.hero p{position:absolute;top:257px;left:0;right:0;font-size:28px;font-weight:700}
.btn-solid{position:absolute;top:326px;left:523px;width:154px;height:47px;background:var(--yellow);color:var(--white);font-size:16px;display:flex;align-items:center;justify-content:center}
.dots{display:flex;gap:8px;justify-content:center}
.dots i{width:8px;height:8px;border-radius:50%;background:var(--white);display:block}
.dots i.on{background:var(--accent-red)}
.hero .dots{position:absolute;bottom:34px;left:0;right:0}

.section-title{font-size:36px;font-weight:300;color:#333;text-align:center}
.btn-outline{display:inline-flex;align-items:center;justify-content:center;height:47px;border:1.5px solid var(--blue-line);color:#333;font-size:15px;padding:0 32px;background:var(--white)}

.welcome{height:342px;text-align:center;padding-top:50px}
.welcome p{width:1040px;margin:24px auto 30px;font-size:14.5px;line-height:25px;color:#333}

.services{height:500px;background:var(--light);padding-top:50px}
.cards{position:relative;margin-top:40px;height:330px}
.card{position:absolute;top:0;width:331px;height:330px;color:var(--white);text-align:center;padding:44px 26px 0}
.card h3{font-size:24px;font-weight:400;margin:22px 0 10px;line-height:29px}
.card p{font-size:14.5px;line-height:23px}
.card svg{width:96px;height:80px}
.card-continuity{left:75px;background:var(--orange);clip-path:polygon(0 16px,100% 0,100% 100%,0 309px)}
.card-support{left:434px;background:var(--teal)}
.card-desk{left:795px;background:var(--pink);clip-path:polygon(0 0,100% 16px,100% 309px,0 100%)}

.updates{height:588px;display:flex;padding:62px 75px 0;position:relative}
.updates::after{content:"";position:absolute;left:600px;top:78px;height:452px;border-left:1px solid var(--divider)}
.column{width:490px}
.column + .column{margin-left:75px}
.column h2{font-size:36px;font-weight:300;color:#333;margin-bottom:20px}
.item{display:flex;gap:26px;margin-bottom:34px}
.item > div:last-child{width:420px}
.date{flex:none;width:64px;height:64px;background:var(--yellow);color:var(--white);text-align:center;clip-path:polygon(0 0,100% 8px,100% 100%,0 100%);padding-top:10px;font-weight:700;line-height:1}
.date small{font-size:12px;display:block}
.date b{font-size:27px}
.item h4{font-size:24px;font-weight:400;color:var(--green);line-height:29px;margin-bottom:10px;padding-right:18px}
.item p{font-size:13.5px;line-height:23px;color:#333}
.column .btn-outline{padding:0 22px;margin-top:8px}

.partners{height:379px;background:var(--light);padding-top:38px}
.logos{display:grid;grid-template-columns:repeat(4,253px);gap:12px 14px;margin:36px 0 0 75px}
.logo-tile{height:82px;background:var(--white);display:flex;align-items:center;justify-content:center;gap:10px;font-size:26px;font-weight:700;color:#3a3a3a}
.logo-tile .mark{width:14px;height:14px;background:#3a3a3a;display:block}
.partners .dots{margin-top:34px}
.partners .dots i{background:#888}
.partners .dots i.on{background:var(--accent-red)}

.footer{height:255px;display:flex;padding:50px 75px 0}
.footer-brand{width:277px;padding-top:24px}
.footer-brand .brand{font-size:42px;display:block;margin-bottom:8px}
.footer-brand small{font-size:11px;color:var(--muted);line-height:18px;display:block}
.footer-brand .social{display:flex;gap:18px;margin-top:24px}
.footer-brand .social span{background:#333;width:18px;height:18px}
.fcol{width:260px}
.fcol h5{font-size:22px;font-weight:400;color:var(--green);margin-bottom:14px}
.fcol li{list-style:none;font-size:13px;color:#333;margin-bottom:15px;display:flex;gap:24px;align-items:flex-start;line-height:19px}
.fcol li::before{content:"›";color:#555}
.contact li::before{content:none}
.contact li svg{flex:none;margin-top:3px}
</style>
</head>
<body>

<div class="topbar">
  <div class="call">
    <svg width="12" height="12" viewBox="0 0 24 24"><path fill="#2fa58f" d="M6.6 10.8a15 15 0 006.6 6.6l2.2-2.2c.3-.3.7-.4 1-.2 1.1.4 2.3.6 3.6.6.6 0 1 .4 1 1V20c0 .6-.4 1-1 1A17 17 0 013 4c0-.6.4-1 1-1h3.5c.6 0 1 .4 1 1 0 1.3.2 2.5.6 3.6.1.3 0 .7-.2 1z"/></svg>
    CALL US: 1-800-555-0142
  </div>
  <div class="social"><span></span><span></span><span></span><span></span><span></span></div>
  <a class="login" href="#">
    <svg width="11" height="11" viewBox="0 0 24 24"><circle cx="12" cy="7" r="5" fill="#fff"/><path d="M2 23c0-6 4.5-9 10-9s10 3 10 9z" fill="#fff"/></svg>
    CUSTOMER LOG IN
  </a>
</div>

<header class="header">
  <a class="brand" href="#">Vale Corvan</a>
  <nav class="nav">
    <a class="active" href="#">HOME</a><a href="#">ABOUT</a><a href="#">SERVICES</a><a href="#">CONTACT</a>
  </nav>
</header>

<section class="hero" role="img" aria-label="City skyline photograph with office towers at dusk">
  <h1>Vale Corvan</h1>
  <p>We are an IT support &amp; security company.</p>
  <a class="btn-solid" href="#">Read More</a>
  <div class="dots"><i class="on"></i><i></i><i></i><i></i></div>
</section>

<section class="welcome">
  <h2 class="section-title">Welcome to Our Website</h2>
  <p>Aliquam molestie, mi et imperdiet euismod, dui purus auctor tellus, et interdum lacus lectus et ante. Sed accumsan sollicitudin sapien, sit amet adipiscing turpis gravida ac. In congue, neque ac lobortis volutpat, libero mauris varius mi, vitae suscipit ipsum ligula vitae risus. Duis aliquam nibh a dui iaculis viverra id a velit. Vivamus egestas risus in magna varius commodo. Sed semper viverra egestas.</p>
  <a class="btn-outline" href="#">Read More</a>
</section>

<section class="services">
  <h2 class="section-title">Our Services</h2>
  <div class="cards">
    <div class="card card-continuity">
      <svg viewBox="0 0 96 80"><circle cx="48" cy="40" r="26" fill="none" stroke="#fff" stroke-width="6"/><path d="M58 14h22l-6-7M38 66H16l6 7" fill="none" stroke="#fff" stroke-width="5" stroke-linecap="round" stroke-linejoin="round"/><rect x="38" y="30" width="20" height="20" fill="none" stroke="#fff" stroke-width="4"/></svg>
      <h3>Business Continuity</h3>
      <p>Vestibulum ante ipsum primis in faucibus orci luctus et ultrices posuere cubilia a nibh eget turpis vehicula tempus ac sed massa lobortis turpis..</p>
    </div>
    <div class="card card-support">
      <svg viewBox="0 0 96 80"><path d="M24 44V36a24 24 0 0148 0v8" fill="none" stroke="#fff" stroke-width="6"/><rect x="16" y="38" width="14" height="22" rx="4" fill="#fff"/><rect x="66" y="38" width="14" height="22" rx="4" fill="#fff"/><path d="M73 60c0 10-10 14-20 14" fill="none" stroke="#fff" stroke-width="4"/><circle cx="50" cy="74" r="4" fill="#fff"/></svg>
      <h3>IT Support &amp; Field Services</h3>
      <p>Vestibulum ante ipsum primis in faucibus orci luctus et ultrices posuere cubilia a nibh eget turpis vehicula..</p>
    </div>
    <div class="card card-desk">
      <svg viewBox="0 0 96 80"><circle cx="48" cy="40" r="34" fill="#fff"/><g fill="none" stroke="#ee4f6a" stroke-width="4"><ellipse cx="48" cy="40" rx="14" ry="34"/><path d="M14 40h68M48 6v68M20 22h56M20 58h56"/></g></svg>
      <h3>Outsourced Service Desk</h3>
      <p>Vestibulum ante ipsum primis in faucibus orci luctus et ultrices posuere cubilia a nibh eget turpis vehicula tempus ac sed massa lobortis turpis..</p>
    </div>
  </div>
</section>

<section class="updates">
  <div class="column">
    <h2>Latest News</h2>
    <div class="item"><div class="date"><small>FEB</small><b>08</b></div><div><h4>Nam fermentum vestibulum purus id aliquet</h4><p>Vestibulum ante ipsum primis in faucibus orci luctus et ultrices posuere cubilia a nibh eget turpis vehicula tempus ac sed massa lobortis turpis..</p></div></div>
    <div class="item"><div class="date"><small>FEB</small><b>08</b></div><div><h4>Nam fermentum vestibulum purus id aliquet</h4><p>Vestibulum ante ipsum primis in faucibus orci luctus et ultrices posuere cubilia a nibh eget turpis vehicula tempus ac sed massa lobortis turpis..</p></div></div>
    <a class="btn-outline" href="#">Read All News</a>
  </div>
  <div class="column">
    <h2>Latest Blog</h2>
    <div class="item"><div class="date"><small>FEB</small><b>08</b></div><div><h4>Nam fermentum vestibulum purus id aliquet</h4><p>Vestibulum ante ipsum primis in faucibus orci luctus et ultrices posuere cubilia a nibh eget turpis vehicula tempus ac sed massa lobortis turpis..</p></div></div>
    <div class="item"><div class="date"><small>FEB</small><b>08</b></div><div><h4>Nam fermentum vestibulum purus id aliquet</h4><p>Vestibulum ante ipsum primis in faucibus orci luctus et ultrices posuere cubilia a nibh eget turpis vehicula tempus ac sed massa lobortis turpis..</p></div></div>
    <a class="btn-outline" href="#">Read All Posts</a>
  </div>
</section>

<section class="partners">
  <h2 class="section-title">Partners</h2>
  <div class="logos">
    <div class="logo-tile"><span class="mark"></span>Quenbrix</div>
    <div class="logo-tile">Brackvel</div>
    <div class="logo-tile">Pendrulo</div>
    <div class="logo-tile">Halvorne</div>
    <div class="logo-tile">Ostrevin</div>
    <div class="logo-tile">Kelvane</div>
    <div class="logo-tile"><span class="mark"></span>Marrowvex</div>
    <div class="logo-tile">Tessory</div>
  </div>
  <div class="dots"><i class="on"></i><i></i><i></i></div>
</section>

<footer class="footer">
  <div class="footer-brand">
    <span class="brand">Vale Corvan</span>
    <small>Copyright © 2018 Company Name<br>All Right Reserved</small>
    <div class="social"><span></span><span></span><span></span><span></span><span></span></div>
  </div>
  <div class="fcol">
    <h5>Services</h5>
    <ul><li>Business Continuity</li><li>IT Support &amp; Field Service</li><li>Outsourced Service Desk</li></ul>
  </div>
  <div class="fcol">
    <h5>Resources</h5>
    <ul><li>IT Services Data Sheet</li><li>Managed IT Support Data Sheet</li><li>Business Continuity Checklist</li></ul>
  </div>
  <div class="fcol contact">
    <h5>Contact</h5>
    <ul>
      <li><svg width="11" height="13" viewBox="0 0 24 28"><path d="M12 0a10 10 0 0110 10c0 7-10 18-10 18S2 17 2 10A10 10 0 0112 0z" fill="#333"/><circle cx="12" cy="10" r="4" fill="#fff"/></svg>4120 Ashwell Road,<br>Leeds, LS9 2QT</li>
      <li><svg width="12" height="12" viewBox="0 0 24 24"><path fill="#333" d="M6.6 10.8a15 15 0 006.6 6.6l2.2-2.2c.3-.3.7-.4 1-.2 1.1.4 2.3.6 3.6.6.6 0 1 .4 1 1V20c0 .6-.4 1-1 1A17 17 0 013 4c0-.6.4-1 1-1h3.5c.6 0 1 .4 1 1 0 1.3.2 2.5.6 3.6.1.3 0 .7-.2 1z"/></svg>1-800-555-0142</li>
      <li><svg width="13" height="10" viewBox="0 0 26 20"><rect width="26" height="20" fill="#333"/><path d="M1 1l12 10L25 1" fill="none" stroke="#fff" stroke-width="2"/></svg>hello@valecorvan.com</li>
    </ul>
  </div>
</footer>

</body>
</html>
```